Engineering Consultant Business Card

I'm starting a new business as a high-end engineering consultant in a niche field. I've attached the jpg for my logo plus the branding guideline document that I've been following. You can see my business website here: www.orvalink.com
I'd like a business card that has the logo on one side, then the other side has (in any order): Tessmor Pact, Inc.
Delia Whitcombe
President and Chief EMC Engineer
www.orvalink.com
delia@orvalink.com
Optional: motto "We will solve your EMC problems as early as possible—ideally before they even start."
I'm not planning on including a phone number
Target Market(s)
Businesses, especially makers of electronics hardware
Industry/Entity Type
Electrical engineering
Contact Information for Business Card
Company name, my name, website, email
Look and feel
Each slider illustrates characteristics of the customer's brand and the style your logo design should communicate.

```html
<!DOCTYPE html>
<html lang="en">
<head>
<meta charset="utf-8">
<title>Tessmor Pact, Inc. — Business Card</title>
<link rel="stylesheet" href="https://fonts.googleapis.com/css2?family=Montserrat:wght@400;500;700;800&display=swap">
<style>
  :root {
    --stage: #3a3a3a;
    --brand-blue: #2a4a9e;
    --brand-blue-deep: #25428f;
    --ink: #1c1c1c;
    --paper: #ffffff;
    --emboss: #2f52a8;
  }
  * { box-sizing: border-box; margin: 0; padding: 0; }
  html, body {
    width: 1200px;
    height: 1200px;
    overflow: hidden;
    background: var(--stage);
    font-family: "Montserrat", sans-serif;
  }
  .card {
    position: absolute;
    left: 250px;
    width: 700px;
    height: 400px;
    box-shadow: 0 14px 30px rgba(0,0,0,0.45);
  }
  .card--back {
    top: 130px;
    background: var(--brand-blue);
    display: flex;
    align-items: center;
    justify-content: center;
  }
  .back-mark {
    display: flex;
    align-items: center;
    gap: 18px;
    color: var(--emboss);
    font-weight: 800;
    font-size: 56px;
    letter-spacing: 4px;
  }
  .back-mark .mark-dot {
    width: 46px; height: 46px;
    border: 6px solid var(--emboss);
    border-radius: 50%;
  }
  .card--front {
    top: 640px;
    background: var(--paper);
  }
  .front-rule {
    position: absolute;
    left: 0; right: 0;
    top: 200px;
    height: 2px;
    background: var(--brand-blue);
  }
  .holder {
    position: absolute;
    top: 34px;
    left: 200px;
  }
  .holder-name {
    color: var(--brand-blue);
    font-weight: 800;
    font-size: 32px;
    line-height: 1;
  }
  .holder-title {
    color: var(--ink);
    font-weight: 400;
    font-size: 17px;
    margin-top: 6px;
  }
  .front-mark {
    position: absolute;
    left: 50%;
    top: 200px;
    transform: translate(-50%, -50%);
    background: var(--paper);
    padding: 10px 26px;
    display: flex;
    align-items: center;
    gap: 14px;
    color: var(--brand-blue);
    font-weight: 800;
    font-size: 48px;
    letter-spacing: 3px;
  }
  .front-mark .mark-dot {
    width: 40px; height: 40px;
    border: 6px solid var(--brand-blue);
    border-radius: 50%;
  }
  .contact {
    position: absolute;
    left: 0; right: 0;
    top: 268px;
    text-align: center;
  }
  .contact-line {
    color: var(--ink);
    font-weight: 400;
    font-size: 18px;
    line-height: 1.5;
  }
  .contact-address {
    color: var(--brand-blue);
    font-weight: 700;
    font-size: 19px;
    margin-top: 16px;
  }
</style>
</head>
<body>
  <section class="card card--back" aria-label="Card back">
    <div class="back-mark"><span class="mark-dot"></span><span>TESSMOR</span></div>
  </section>

  <section class="card card--front" aria-label="Card front">
    <div class="front-rule"></div>
    <div class="holder">
      <p class="holder-name">Delia Whitcombe</p>
      <p class="holder-title">President &amp; Chief EMC Engineer</p>
    </div>
    <div class="front-mark"><span class="mark-dot"></span><span>TESSMOR</span></div>
    <div class="contact">
      <p class="contact-line">delia@orvalink.com</p>
      <p class="contact-line">www.orvalink.com</p>
      <p class="contact-address">1740 NE Harbor Ridge Rd Kelton, Florida 34210</p>
    </div>
  </section>
</body>
</html>
```